Delmer's Pressure Washing Services

Starting a pressure washing business on my own in Central Valley California, not too much experience so affordable, I do houses, fences, driveways, cars, trailers, RVs. Planning to make this full-time hoping clientele picks up after having a nice business card. Design doesn't have to be flashy, more to the point, I like simplistic/personable. I do not want something exhausting to look at or with too much going on.

Target Market(s)

Residential, Commercial

Industry/Entity Type

Pressure Washing

Contact Information for Business Card

avalible Services

Font styles to use
Sans Serif

Colors
0054AA
0677BA
7BADD7
CADEEF
E8F1F8
0094D4
00A9DD
6FCCEA
C7EBF8
E9F6FB
00AB8E
00BBA5
67D7C9
C6EFE9
E9F9F6

```html
<!DOCTYPE html>
<html lang="en">
<head>
<meta charset="utf-8">
<title>Delmer's Pressure Washing Services – Business Card</title>
<link rel="stylesheet" href="https://fonts.googleapis.com/css2?family=Arimo:wght@400;700&display=swap">
<style>
  :root {
    --backdrop: #9fcfa5;
    --card-black: #231f20;
    --spray-blue: #6ccaea;
    --ink-white: #ffffff;
    --ink-dark: #231f20;
  }
  html, body {
    margin: 0;
    padding: 0;
    width: 1200px;
    height: 900px;
    overflow: hidden;
    background: var(--backdrop);
    font-family: "Arimo", Arial, sans-serif;
  }
  .canvas {
    position: relative;
    width: 1200px;
    height: 900px;
  }
  .card {
    position: absolute;
    left: 250px;
    width: 700px;
    height: 400px;
    box-shadow: 0 10px 24px rgba(0, 0, 0, 0.25);
  }
  .card svg { display: block; width: 700px; height: 400px; }
  .card--front { top: 30px; }
  .card--back { top: 470px; }

  .fill-black { fill: var(--card-black); }
  .fill-blue { fill: var(--spray-blue); }
  .stroke-dark { stroke: var(--ink-dark); stroke-width: 2; }

  .label-role { fill: var(--ink-white); font-size: 15px; letter-spacing: 0.5px; }
  .label-owner { fill: var(--spray-blue); font-size: 25px; letter-spacing: 1.5px; }
  .company-name { fill: var(--ink-dark); font-size: 24px; font-weight: 700; letter-spacing: 2px; }
  .company-tagline { fill: var(--ink-dark); font-size: 15px; letter-spacing: 0.5px; }
  .service-list { fill: var(--ink-dark); font-size: 17px; letter-spacing: 0.5px; }
  .phone-number { fill: var(--spray-blue); font-size: 21px; letter-spacing: 1px; }

  .brand-name { fill: var(--spray-blue); font-size: 64px; font-weight: 700; letter-spacing: 2px; }
  .brand-sub { fill: var(--spray-blue); font-size: 22px; font-weight: 700; letter-spacing: 3px; }
</style>
</head>
<body>
<main class="canvas">

  <section class="card card--front" aria-label="Business card front">
    <svg viewBox="0 0 700 400" xmlns="http://www.w3.org/2000/svg">
      <rect class="fill-black" width="700" height="400"/>
      <polygon class="fill-blue" points="0,172 700,22 700,318 0,246"/>

      <text class="label-role" x="60" y="42">proprietor</text>
      <text class="label-owner" x="60" y="72">Delmer Ortiz</text>

      <text class="company-name" x="232" y="188" text-anchor="middle">DELMER'S</text>
      <text class="company-tagline" x="232" y="212" text-anchor="middle">PRESSURE WASHING SERVICES</text>

      <line class="stroke-dark" x1="420" y1="98" x2="420" y2="278"/>

      <g class="service-list">
        <text x="440" y="108">• HOUSEs</text>
        <text x="440" y="140">• FENCEs</text>
        <text x="440" y="172">• DRIVEWAYs</text>
        <text x="440" y="204">• CARs</text>
        <text x="440" y="236">• TRAILERs</text>
        <text x="440" y="268">• RVs</text>
      </g>

      <g transform="translate(268,352)">
        <path class="fill-blue" d="M2,-18 q-8,3 -4,15 q5,11 17,10 l2,-6 l-7,-4 l-3,3 q-6,-2 -7,-9 l3,-2 l-1,-8 z"/>
        <circle class="fill-blue" cx="24" cy="-2" r="2"/>
        <circle class="fill-blue" cx="31" cy="-2" r="2"/>
        <circle class="fill-blue" cx="38" cy="-2" r="2"/>
        <text class="phone-number" x="46" y="0">2095550148</text>
      </g>
    </svg>
  </section>

  <section class="card card--back" aria-label="Business card back">
    <svg viewBox="0 0 700 400" xmlns="http://www.w3.org/2000/svg">
      <rect class="fill-black" width="700" height="400"/>
      <polygon class="fill-blue" points="700,95 700,150 470,190"/>

      <circle class="fill-blue" cx="140" cy="205" r="14"/>
      <text class="brand-name" x="170" y="228">Delmer's</text>
      <text class="brand-sub" x="172" y="268">PRESSURE WASHING SERVICES</text>
    </svg>
  </section>

</main>
</body>
</html>
```